First Reponders Promotion poster/flyer

Our Yoga studio is introducing an ongoing promotion for all First Responders, Police/Nurse/Paramedic/Firefighters/Doctors
$22pw for Unlimited access to our Inner city Studio which will become a sanctuary for the people who look after us. Tag line: You look after us, let us look after you. The benefits of yoga, reduce stress, clear mind, healthy body. Feel free to use other assets, and be as creative as you like I have just put images and designs as a guide.

Target Market(s)

Emergency Services Tasmania

Industry/Entity Type

Emergency Services

Requirements
Must have
• Stillwave Logo/Address 41 Marlow St/ website www.stillwavestudio.com.a/ sign up online and just bring in current work Id at checkin/$22pw Unlimited classes/Australian market so can't look like usa or any other countries
Nice to have
• words , inner city Sanctuary
Should not have
• Foreign Country images

```html
<!DOCTYPE html>
<html lang="en">
<head>
<meta charset="utf-8">
<title>Stillwave – First Responders Promotion</title>
<link rel="stylesheet" href="https://fonts.googleapis.com/css2?family=Oswald:wght@200;300;400;500;600;700&family=Open+Sans:wght@600&display=swap">
<style>
  :root {
    --ink: #000000;
    --paper: #ffffff;
    --gold: #eeae33;
  }
  * { margin: 0; padding: 0; box-sizing: border-box; }
  html, body { width: 888px; height: 1200px; overflow: hidden; background: var(--ink); }
  .poster {
    position: relative; width: 888px; height: 1200px;
    background: var(--ink); color: var(--paper);
    font-family: "Oswald", "Arial Narrow", sans-serif;
  }
  .poster > * { position: absolute; }
  .headline-light {
    left: 40px; width: 808px; top: 30px;
    font-weight: 200; font-size: 61px; line-height: 1; text-align: center; white-space: nowrap;
  }
  .headline-bold {
    left: 40px; width: 808px; top: 93px;
    font-weight: 600; font-size: 53px; line-height: 1; text-align: center; white-space: nowrap;
  }
  .sanctuary-band {
    left: 40px; width: 808px; top: 156px; height: 81px;
    background: var(--gold); color: var(--paper);
    font-weight: 700; font-size: 82px; line-height: 81px; text-align: center;
    white-space: nowrap; letter-spacing: -0.5px;
  }
  .rule { left: 40px; width: 808px; height: 2px; background: var(--gold); }
  .rule--top { top: 250px; }
  .rule--bottom { top: 305px; }
  .benefits {
    left: 40px; width: 808px; top: 260px;
    font-family: "Open Sans", Arial, sans-serif; font-weight: 600;
    font-size: 29px; line-height: 40px; text-align: center; white-space: nowrap;
  }
  .address-box {
    left: 40px; top: 316px; width: 247px; height: 94px;
    background: var(--gold); color: var(--ink); padding-left: 14px;
  }
  .address-street { font-weight: 600; font-size: 30px; line-height: 1; margin-top: 4px; }
  .address-city { font-weight: 500; font-size: 62px; line-height: 1; margin-top: -4px; }
  .launch-date {
    left: 304px; width: 544px; top: 300px;
    font-weight: 600; font-size: 108px; line-height: 1.2; white-space: nowrap; text-align: center;
  }
  .launch-date sup { font-size: 48px; vertical-align: 48px; line-height: 0; }
  .photo-grid { left: 39px; top: 420px; width: 808px; height: 278px; background: var(--gold); }
  .photo-grid .white-panel { position: absolute; left: 0; top: 0; width: 274px; height: 278px; background: var(--paper); }
  .photo { position: absolute; }
  .photo--firefighter { left: 11px; top: 10px; width: 251px; height: 258px;
    background: linear-gradient(160deg, #9a8a70 0%, #6e5a3e 50%, #c8b23a 100%); }
  .photo--nurse { left: 284px; top: 10px; width: 243px; height: 123px;
    background: linear-gradient(180deg, #e8e8e6 0%, #d9dcd8 55%, #5f7a72 100%); }
  .photo--care { left: 284px; top: 145px; width: 243px; height: 123px;
    background: linear-gradient(160deg, #6f8290 0%, #8aa0ad 50%, #c99a7c 100%); }
  .photo--paramedic { left: 542px; top: 10px; width: 250px; height: 183px;
    background: linear-gradient(150deg, #3d6a3a 0%, #1e2a48 55%, #d9c36a 100%); }
  .photo--police { left: 542px; top: 203px; width: 250px; height: 65px;
    background: linear-gradient(90deg, #2d333d 0%, #b9c94a 50%, #2d333d 100%); }
  .roles-primary {
    left: 0; width: 888px; top: 705px;
    font-weight: 600; font-size: 51px; line-height: 1.1; text-align: center; white-space: nowrap;
  }
  .roles-secondary {
    left: 0; width: 888px; top: 762px;
    font-weight: 600; font-size: 36px; line-height: 1.1; text-align: center; white-space: nowrap;
  }
  .signup-band {
    left: 40px; width: 808px; top: 811px; height: 38px;
    background: var(--gold); color: var(--paper);
    font-weight: 300; font-size: 28px; line-height: 38px; text-align: center; white-space: nowrap;
  }
  .contract-question {
    left: 40px; top: 860px; width: 184px; height: 69px;
    background: var(--paper); color: var(--ink);
    font-weight: 600; font-size: 27px; line-height: 31px; letter-spacing: 1px;
    padding: 3px 0 0 8px;
  }
  .contract-answer {
    left: 224px; top: 860px; width: 621px; height: 69px;
    border: 2px solid var(--paper); color: var(--gold);
    font-weight: 300; font-size: 38px; line-height: 65px; text-align: center; white-space: nowrap;
  }
  .tagline-copy {
    left: 0; width: 888px; top: 938px;
    font-weight: 300; font-size: 18.5px; line-height: 23px; letter-spacing: 1.5px; text-align: center;
  }
  .tagline-band {
    left: 40px; width: 808px; top: 996px; height: 44px;
    background: var(--gold); color: var(--ink);
    font-weight: 600; font-size: 33px; line-height: 44px; letter-spacing: 3px; text-align: center; white-space: nowrap;
  }
  .brand-box {
    left: 40px; top: 1055px; width: 332px; height: 108px;
    background: var(--paper); color: var(--ink);
    display: flex; flex-direction: column; align-items: center; justify-content: center; gap: 12px;
  }
  .brand-row { display: flex; align-items: center; gap: 14px; }
  .brand-mark { width: 16px; height: 16px; background: var(--gold); }
  .brand-name { font-weight: 400; font-size: 32px; line-height: 1; letter-spacing: 10px; text-transform: uppercase; }
  .brand-website { font-weight: 400; font-size: 15px; line-height: 1; letter-spacing: 2px; }
  .promo-box {
    left: 386px; top: 1055px; width: 459px; height: 108px;
    background: var(--paper); color: var(--ink);
  }
  .promo-label { position: absolute; left: 10px; top: 12px; font-weight: 600; line-height: 1; }
  .promo-label span { display: block; }
  .promo-label .small { font-size: 32px; }
  .promo-label .large { font-size: 54px; }
  .promo-price {
    position: absolute; right: 10px; top: -4px;
    color: var(--gold); font-weight: 700; font-size: 104px; line-height: 1.1; letter-spacing: -2px;
  }
</style>
</head>
<body>
<main class="poster">
  <h1 class="headline-light">UNLIMITED ACCESS TO OUR CLASSES</h1>
  <h2 class="headline-bold">IN OUR BEAUTIFUL INNER-CITY STUDIO</h2>
  <div class="sanctuary-band">SANCTUARY FOR $22PW</div>

  <div class="rule rule--top"></div>
  <p class="benefits">YOGA HELPS STRESS, MENTAL HEALTH, FITNESS</p>
  <div class="rule rule--bottom"></div>

  <div class="address-box">
    <div class="address-street">41 MARLOW ST</div>
    <div class="address-city">HOBART</div>
  </div>
  <div class="launch-date">1<sup>ST</sup> JULY 2022</div>

  <section class="photo-grid">
    <div class="white-panel"></div>
    <div class="photo photo--firefighter" role="img" aria-label="Firefighter in turnout gear and breathing mask"></div>
    <div class="photo photo--nurse" role="img" aria-label="Nurse in scrubs holding a clipboard"></div>
    <div class="photo photo--care" role="img" aria-label="Nurse holding a patient's hands"></div>
    <div class="photo photo--paramedic" role="img" aria-label="Paramedic in uniform seen from behind"></div>
    <div class="photo photo--police" role="img" aria-label="Police officer in high-visibility vest"></div>
  </section>

  <p class="roles-primary">PARAMEDIC/AMBULANCE/NURSE</p>
  <p class="roles-secondary">POLICE/FIREFIGHTERS/SES/DOCTORS</p>
  <div class="signup-band">JUST SIGN UP ON WEBSITE AND BRING IN YOU CURRENT ID FOR VERIFICATION</div>

  <div class="contract-question">IS THERE ANY<br>CONTRACT ?</div>
  <div class="contract-answer">NO ONLY EMAIL 2 WEEKS PRIOR TO CANCEL</div>

  <p class="tagline-copy">YOU LOOK AFTER US, LET US LOOK AFTER YOU. THE BENEFITS OF YOGA, REDUCE STRESS<br>CLEAR MIND, HEALTHY BODY. FEEL FREE TO USE OTHER ASSETS</p>
  <div class="tagline-band">YOU LOOK AFTER US, LET US LOOK AFTER YOU!</div>

  <div class="brand-box">
    <div class="brand-row">
      <span class="brand-mark"></span>
      <span class="brand-name">Stillwave</span>
    </div>
    <span class="brand-website">www.stillwavestudio.com.a</span>
  </div>
  <div class="promo-box">
    <div class="promo-label"><span class="small">PROMO OF</span><span class="large">PRICE</span></div>
    <div class="promo-price">$22PW</div>
  </div>
</main>
</body>
</html>
```